Wordpress Design Project

I currently have a temporary website at www.dorrankeadvisors.com this site provides a good sample of the information which needs to be included on the website. As you will see the design is very basic and does not include the company logo or any reference to the colors of the logo.

A couple of webpages which I really like and should provide an indication:
- plinvo.com
- brosket.it (good client log in, dont like dark colors)
- pixel harbor
- tulmora.com

I have also added the company logo and my business card which provide some idea of coloring etc.

Industry/Entity Type

Business

Requirements
Must have
• - Blog Page - see blog.plinvo.com for a good example;
- Client log-in;
- Twitter linkage;
- linkedin linkage;
- mobile browser scale ability;

```html
<!DOCTYPE html>
<html lang="en">
<head>
<meta charset="utf-8">
<title>Dorranke Advisors – Business Advisors</title>
<link href="https://fonts.googleapis.com/css2?family=Cabin:wght@400;600;700&family=Arimo:ital,wght@0,400;1,400&family=EB+Garamond:wght@400&display=swap" rel="stylesheet">
<style>
:root{
  --blue-dark:#2a6aa3;
  --blue:#3a86c4;
  --blue-light:#5aa2d6;
  --accent-blue:#1a6bb8;
  --orange:#f79a1e;
  --orange-deep:#f0820f;
  --text:#3c3c3c;
  --muted:#6a6a6a;
  --panel:#f5f5f5;
  --footer:#2f2f2f;
  --footer-text:#d8d8d8;
}
*{box-sizing:border-box;margin:0;padding:0}
html,body{width:1103px;height:1200px;overflow:hidden}
body{position:relative;background:#fff;font-family:'Arimo',Arial,sans-serif;color:var(--text)}

.site-header{position:absolute;left:0;top:0;width:1103px;height:101px;
  background:linear-gradient(#3d86c2,#2d6fa9);border-bottom:4px solid var(--orange)}
.brand-box{position:absolute;left:94px;top:0;width:210px;height:129px;background:linear-gradient(#fff,#f1f1f1);
  box-shadow:0 4px 10px rgba(0,0,0,.25);z-index:3;display:flex;flex-direction:column;align-items:center;justify-content:center;gap:6px}
.brand-name{font-family:'EB Garamond',Georgia,serif;font-size:25px;color:#2b5c8f;display:flex;align-items:center;gap:8px;white-space:nowrap}
.brand-mark{width:14px;height:14px;border-radius:50%;background:var(--orange)}
.brand-tag{font-family:'EB Garamond',Georgia,serif;font-size:11px;letter-spacing:5px;color:#2b5c8f}

.main-nav{position:absolute;top:0;left:0;height:97px;width:1103px}
.nav-item{position:absolute;top:54px;font-family:'Cabin',sans-serif;font-weight:600;font-size:14px;color:#fff;transform:translateX(-50%)}
.nav-home{position:absolute;left:379px;top:30px;width:69px;height:67px;border-radius:4px 4px 0 0;
  background:linear-gradient(#fdc02c,var(--orange-deep));color:#3a2a10;font-family:'Cabin',sans-serif;font-weight:700;font-size:13px;
  display:flex;align-items:center;justify-content:center;padding-bottom:2px}

.hero{position:absolute;left:0;top:101px;width:1103px;height:415px;
  background:linear-gradient(100deg,#cfd9e1 0%,#e9eef2 35%,#f4f6f8 55%,#c9d0d8 80%,#9aa4ae 100%)}
.hero-arrow{position:absolute;top:254px;width:44px;height:44px;border-radius:50%;background:rgba(160,170,180,.55)}
.hero-arrow svg{width:44px;height:44px}

.intro{position:absolute;left:0;top:516px;width:1103px;height:293px;background:var(--panel)}
.intro-brand{position:absolute;left:95px;top:36px;display:flex;flex-direction:column;gap:4px}
.intro-brand .brand-name{font-size:26px}
.intro-rule{position:absolute;left:95px;top:105px;width:612px;height:1px;background:#d4d4d4}
.intro-rule::before{content:"";position:absolute;left:0;top:-1px;width:137px;height:3px;background:#c8c8c8}
.intro-copy{position:absolute;left:95px;top:117px;width:622px;font-size:12.2px;line-height:16.5px;color:var(--text)}
.intro-copy p+p{margin-top:16.5px}
.more{font-style:italic;font-size:11px;color:var(--accent-blue);position:absolute;display:flex;align-items:center;gap:2px}
.more b{color:#333;font-style:normal;font-size:10px;letter-spacing:-2px}
.intro-divider{position:absolute;left:727px;top:55px;height:220px;border-left:1px dotted #c8c8c8}

.login{position:absolute;left:743px;top:52px;width:268px;height:202px;border:1px solid #ddd;border-radius:8px;
  background:linear-gradient(#fff,#f0f0f0);box-shadow:0 1px 3px rgba(0,0,0,.1);overflow:hidden}
.login h2{position:absolute;left:11px;top:22px;font-family:'Cabin',sans-serif;font-weight:600;font-size:18.5px;color:var(--accent-blue)}
.login h2 span{color:var(--orange)}
.login-corner{position:absolute;right:0;top:0;width:85px;height:75px}
.field{position:absolute;left:12px;font-size:11.5px;color:#444;display:flex;align-items:center}
.field label{width:66px}
.field .input{width:139px;height:24px;border-radius:12px;border:1px solid #ddd;background:linear-gradient(#eee,#f8f8f8)}
.forgot{position:absolute;left:48px;top:158px;font-size:11.5px;color:#333}
.login-btn{position:absolute;left:154px;top:150px;width:71px;height:26px;border-radius:4px;
  background:linear-gradient(#5aa8e6,#1b6cb5);border:1px solid #1a5c99;color:#fff;font-family:'Cabin',sans-serif;font-size:14px;
  display:flex;align-items:center;justify-content:center}

.services{position:absolute;left:0;top:809px;width:1103px;height:306px}
.service{position:absolute;top:0;width:235px}
.service h3{position:absolute;top:37px;left:0;white-space:nowrap;font-family:'Cabin',sans-serif;font-weight:600;font-size:20px;color:var(--accent-blue)}
.service h3 span{color:var(--orange)}
.service-photo{position:absolute;top:68px;left:0;width:235px;height:108px;background:#d6d6d6;padding:8px}
.service-photo div{width:100%;height:100%;border:1px solid #fff}
.service p{position:absolute;top:194px;left:0;width:235px;font-size:11.5px;line-height:16.5px;color:#333;text-align:justify}
.service .more{right:0;top:258px}
.col-divider{position:absolute;top:67px;height:210px;border-left:1px dotted #bbb}

.site-footer{position:absolute;left:0;top:1115px;width:1103px;height:85px;background:var(--footer)}
.footer-brand{position:absolute;left:112px;top:18px;display:flex;flex-direction:column;gap:4px}
.footer-brand .brand-name{color:#c9c9c9;font-size:27px}
.footer-brand .brand-mark{background:#9a9a9a}
.footer-brand .brand-tag{color:#b8b8b8}
.social{position:absolute;left:466px;top:23px;display:flex;gap:11px}
.social span{width:26px;height:26px;border-radius:5px;background:linear-gradient(#e6e6e6,#a9a9a9)}
.footer-links{position:absolute;right:105px;top:22px;text-align:right;font-size:11.5px;color:var(--footer-text);line-height:22px;letter-spacing:.3px}
</style>
</head>
<body>

<header class="site-header"></header>
<div class="brand-box">
  <div class="brand-name"><span class="brand-mark"></span>Dorranke Advisors</div>
  <div class="brand-tag">Business Advisors</div>
</div>
<nav class="main-nav">
  <a class="nav-home">HOME</a>
  <span class="nav-item" style="left:514px">Consulting</span>
  <span class="nav-item" style="left:633px">Accounting</span>
  <span class="nav-item" style="left:748px">Partners</span>
  <span class="nav-item" style="left:850px">About Us</span>
  <span class="nav-item" style="left:961px">Contact Us</span>
</nav>

<section class="hero" role="img" aria-label="Photo of a business team meeting with a presenter at a flip chart">
  <div class="hero-arrow" style="left:19px"><svg viewBox="0 0 44 44"><path d="M25 15 L18 22 L25 29" fill="none" stroke="#fff" stroke-width="3"/></svg></div>
  <div class="hero-arrow" style="left:1030px"><svg viewBox="0 0 44 44"><path d="M19 15 L26 22 L19 29" fill="none" stroke="#fff" stroke-width="3"/></svg></div>
</section>

<section class="intro">
  <div class="intro-brand">
    <div class="brand-name"><span class="brand-mark"></span>Dorranke Advisors</div>
    <div class="brand-tag">Business Advisors</div>
  </div>
  <div class="intro-rule"></div>
  <div class="intro-copy">
    <p>Dorranke Advisors is a business advisory firm focuses on assisting businesses reach their potential. We understand and are passionate about small and medium sized businesses. Through the provision of sound long term advice we aim to build strong ongoing relationships with our clients.</p>
    <p>We offer business ongoing accounting services and advice, as well as provide consulting services to help businesses through difficult times. As a Chartered Accounting Firm with a strong technical accounting background and considerable experience in assisting business dealing with significant issues within their business. Dorranke Advisors can assist your business reach its full potential.</p>
  </div>
  <a class="more" style="left:641px;top:326px;top:326px;position:absolute;top:326px"></a>
  <a class="more" style="left:641px;top:326px"></a>
  <span class="more" style="left:641px;top:327px;top:327px"></span>
  <span class="more" style="left:641px;top:327px"></span>
  <span class="more" style="right:390px;top:326px;right:auto;left:641px;top:326px"></span>
  <span class="more" style="left:641px;top:326px"></span>
  <div class="intro-divider"></div>

  <div class="login">
    <h2>Member Area-<span>Login</span></h2>
    <svg class="login-corner" viewBox="0 0 85 75"><path d="M0 0 H85 V75 Z" fill="#e6a21c"/><path d="M0 0 L38 75 L85 75" fill="#d8d8d8" opacity=".0"/><path d="M0 0 Q22 48 45 72 Q35 40 0 0Z" fill="#cfcfcf"/></svg>
    <div class="field" style="top:74px"><label>Username :</label><span class="input"></span></div>
    <div class="field" style="top:119px"><label>Password :</label><span class="input"></span></div>
    <div class="forgot">Forgot password ?</div>
    <div class="login-btn">Login</div>
  </div>
</section>
<span class="more" style="left:641px;top:837px">More Details <b>&gt;&gt;</b></span>

<section class="services">
  <article class="service" style="left:118px">
    <h3>Negotiation <span>with Revenue Office</span></h3>
    <div class="service-photo"><div role="img" aria-label="Photo of two hands in a handshake" style="background:linear-gradient(90deg,#c08a68,#9a5a3a 50%,#d8c0b0)"></div></div>
    <p>Vestibulum rutrum pharetra diam, eget dapibus leo vehicula ut. Fusce aliquam, odio eget adipiscing lobortis, nisl sapien placerat est...</p>
    <span class="more">More Details <b>&gt;&gt;</b></span>
  </article>
  <div class="col-divider" style="left:391px"></div>
  <article class="service" style="left:432px">
    <h3>Cash flow <span>Management</span></h3>
    <div class="service-photo"><div role="img" aria-label="Illustration of rising coin stacks with a red growth arrow" style="background:linear-gradient(#fff 40%,#e9d3b0 80%,#c9a04a)"></div></div>
    <p>Vestibulum rutrum pharetra diam, eget dapibus leo vehicula ut. Fusce aliquam, odio eget adipiscing lobortis, nisl sapien placerat est...</p>
    <span class="more" style="top:260px">More Details <b>&gt;&gt;</b></span>
  </article>
  <div class="col-divider" style="left:703px"></div>
  <article class="service" style="left:743px">
    <h3>Business <span>Processes</span></h3>
    <div class="service-photo"><div role="img" aria-label="Photo of hands joining jigsaw puzzle pieces" style="background:radial-gradient(circle at 50% 50%,#f2f2f2 0 18%,#3a3e44 55%,#1e2228)"></div></div>
    <p>Vestibulum rutrum pharetra diam, eget dapibus leo vehicula ut. Fusce aliquam, odio eget adipiscing lobortis, nisl sapien placerat est...</p>
    <span class="more" style="top:262px">More Details <b>&gt;&gt;</b></span>
  </article>
</section>

<footer class="site-footer">
  <div class="footer-brand">
    <div class="brand-name"><span class="brand-mark"></span>Dorranke Advisors</div>
    <div class="brand-tag">Business Advisors</div>
  </div>
  <div class="social" aria-label="Social links">
    <span role="img" aria-label="Social link"></span>
    <span role="img" aria-label="Social link"></span>
    <span role="img" aria-label="Social link"></span>
  </div>
  <div class="footer-links">
    Home ~ Consulting ~ Accounting ~ Partners ~ About Us ~ Contact Us<br>
    Dorranke Advisors Business Advisors, Copyright &nbsp;2013, Privacy Policy
  </div>
</footer>

</body>
</html>
```